BRIGHTFIELD BUILDERS leave behind sales FLYER 8.5"x11"

We need a high quality advertising flyer 8.5"x11" for our construction company offering kitchen and bathroom remodels. Can be front and back or just the front of the flyer depending on the design. phone number to come
www.tarnwickbuildco.example

we are also a home inspection company. We will leave this at the home when we are done with our home inspections for our new home owners

Target Market(s)

Home owners

Industry/Entity Type

Residential Construction

Contact Information for Business Card

We want it to match the flyer please

Requirements
Must have
• My logo, my website , my phone number (to come later),
• FL State Lic. #RBQ4807193 & Insured
• We Specialize in Bathroom and Kitchen remodeling ,new Construction & Interior or Exterior home Renovations, garages and more! Serving Central Florida for over 15 years.
• Family owned and operated,
• we perform all levels of building and remodeling.
• i wouldn't mind seeing what you come up with for text on the flyer.
Nice to have
• maybe a nice kitchen and bathroom pictures

```html
<!DOCTYPE html>
<html lang="en">
<head>
<meta charset="utf-8">
<title>Brightfield Builders Flyer</title>
<link href="https://fonts.googleapis.com/css2?family=Oswald:wght@500;700&family=Open+Sans:ital,wght@0,400;0,600;1,700&display=swap" rel="stylesheet">
<style>
  :root{
    --orange:#f39322;
    --orange-dark:#d9771a;
    --blue:#1e9ad6;
    --blue-dark:#1479b5;
    --ink:#3c3c3c;
    --grey:#5b5d60;
    --paper:#f4f4f4;
    --backdrop:#d9d9d9;
  }
  *{box-sizing:border-box;margin:0;padding:0}
  html,body{width:1200px;height:960px;overflow:hidden}
  body{background:var(--backdrop);font-family:"Open Sans",Arial,sans-serif;color:var(--ink);position:relative}
  .flyer{position:absolute;top:156px;width:508px;height:656px;background:radial-gradient(ellipse at 50% 45%,#ffffff 0%,#ececec 70%,#dedede 100%);overflow:hidden}
  .flyer--front{left:66px}
  .flyer--back{left:624px}
  .frame{position:absolute;inset:0;width:100%;height:100%}
  .photo{position:absolute;border:3px solid #fff;box-shadow:0 2px 4px rgba(0,0,0,.25)}
  .photo--bath{background:linear-gradient(160deg,#e9e6e1,#b8b4ad 60%,#7d7771)}
  .photo--kitchen{background:linear-gradient(160deg,#d8d2c8,#8f867a 60%,#4d4640)}
  .photo--red{background:linear-gradient(160deg,#e5d8d0,#b24a3e 55%,#5a3a33)}
  .brand{position:absolute;left:0;right:0;top:250px;text-align:center}
  .brand__mark{display:block;width:76px;height:76px;background:var(--orange);margin:0 auto 22px}
  .brand__name{font-family:"Oswald",sans-serif;font-weight:700;font-size:42px;letter-spacing:2px;color:var(--grey);line-height:1}
  .brand__sub{font-family:"Oswald",sans-serif;font-weight:700;font-size:20px;letter-spacing:14px;color:var(--grey);line-height:1;margin-top:8px;padding-left:14px}
  .brand__rule{width:300px;height:2px;background:var(--grey);margin:8px auto 0}
  .front__intro{position:absolute;left:40px;right:40px;top:440px;text-align:center;color:var(--orange);font-size:11.5px;line-height:1.3}
  .front__licence{position:absolute;left:0;right:0;top:494px;text-align:center;font-size:9px;font-weight:600;color:var(--grey)}
  .contact{position:absolute;bottom:8px;left:24px;right:24px;display:flex;gap:40px;color:#fff;font-size:13px;align-items:center}
  .contact span{display:flex;align-items:center;gap:6px}
  .back__title{position:absolute;left:16px;top:50px;font-family:"Oswald",sans-serif;font-weight:700;font-size:34px;color:var(--grey)}
  .back__lead{position:absolute;left:16px;top:100px;width:200px;font-size:14.5px;line-height:1.4}
  .back__lead em{font-weight:700;display:block;text-indent:10px}
  .back__lead p{text-indent:10px}
  .gallery{position:absolute;left:222px;top:48px;width:274px;height:300px}
  .gallery__label{position:absolute;color:#fff;font-size:13px}
  .back__guarantee{position:absolute;left:16px;right:16px;top:364px;font-size:14.5px;line-height:1.4;text-indent:12px}
  .services{position:absolute;left:20px;top:434px;display:grid;grid-template-columns:232px 200px;row-gap:2px;list-style:none;font-size:15px;color:var(--grey)}
  .services li{display:flex;align-items:center;gap:6px}
  .back__brand{position:absolute;right:20px;top:530px;text-align:center}
  .back__brand .brand__mark{width:22px;height:22px;margin:0 auto 4px}
  .back__brand .brand__name{font-size:18px;letter-spacing:1px}
  .back__brand .brand__sub{font-size:9px;letter-spacing:6px;margin-top:3px;padding-left:6px}
</style>
</head>
<body>
<svg width="0" height="0" style="position:absolute">
  <defs>
    <symbol id="tick" viewBox="0 0 16 16"><circle cx="7" cy="9" r="6" fill="none" stroke="#f39322" stroke-width="2"/><path d="M3 8l4 4 8-10" fill="none" stroke="#1e9ad6" stroke-width="2.5"/></symbol>
  </defs>
</svg>

<section class="flyer flyer--front">
  <svg class="frame" viewBox="0 0 508 656" aria-hidden="true">
    <polygon points="130,0 508,0 508,12 150,12" fill="var(--orange)"/>
    <polygon points="0,0 110,0 0,40" fill="var(--blue)"/>
    <polygon points="0,50 60,30 60,120 0,140" fill="var(--blue)"/>
    <polygon points="470,20 508,20 508,110 470,90" fill="var(--orange)"/>
    <polygon points="0,520 45,520 45,600 0,610" fill="var(--blue)"/>
    <polygon points="460,540 508,520 508,600 460,600" fill="var(--blue)"/>
    <polygon points="0,612 400,612 420,620 0,620" fill="var(--orange)"/>
    <rect x="0" y="622" width="508" height="34" fill="var(--blue)"/>
    <polygon points="400,600 508,580 508,622 440,622" fill="var(--orange)"/>
  </svg>
  <div class="photo photo--bath" style="left:50px;top:52px;width:145px;height:86px" role="img" aria-label="Remodeled bathroom vanity"></div>
  <div class="photo photo--bath" style="left:208px;top:52px;width:145px;height:86px" role="img" aria-label="Modern bathroom with tub"></div>
  <div class="photo photo--bath" style="left:364px;top:52px;width:145px;height:86px" role="img" aria-label="Bright bathroom with window"></div>

  <div class="brand">
    <span class="brand__mark"></span>
    <div class="brand__name">BRIGHTFIELD</div>
    <div class="brand__sub">BUILDERS</div>
    <div class="brand__rule"></div>
  </div>

  <p class="front__intro">We Specialize in Bathroom and Kitchen remodeling, new Construction &amp; Interior or Exterior home Renovations, garages and more! Serving Central Florida for over 15 years.</p>
  <p class="front__licence">FL State Lic. #RBQ4807193 &amp; Insured</p>

  <div class="photo photo--kitchen" style="left:0;top:515px;width:144px;height:88px" role="img" aria-label="Kitchen with wood cabinets"></div>
  <div class="photo photo--bath" style="left:156px;top:515px;width:144px;height:88px" role="img" aria-label="Grey kitchen with island"></div>
  <div class="photo photo--red" style="left:312px;top:515px;width:144px;height:88px" role="img" aria-label="Kitchen with red backsplash and dining table"></div>

  <div class="contact">
    <span><svg width="14" height="14" viewBox="0 0 16 16"><circle cx="8" cy="8" r="6.5" fill="none" stroke="#fff" stroke-width="1.5"/><path d="M1.5 8h13M8 1.5c-3 3-3 10 0 13M8 1.5c3 3 3 10 0 13" fill="none" stroke="#fff"/></svg>www.tarnwickbuildco.example</span>
    <span><svg width="10" height="14" viewBox="0 0 10 16"><rect x="1" y="1" width="8" height="14" rx="2" fill="none" stroke="#fff" stroke-width="1.5"/><circle cx="5" cy="12.5" r="1" fill="#fff"/></svg>(555) 014-2290</span>
  </div>
</section>

<section class="flyer flyer--back">
  <svg class="frame" viewBox="0 0 508 656" aria-hidden="true">
    <polygon points="0,0 380,0 360,12 0,12" fill="var(--orange)"/>
    <polygon points="400,0 508,0 508,40" fill="var(--blue)"/>
    <polygon points="0,0 20,0 20,40 0,50" fill="var(--blue)"/>
    <polygon points="0,600 120,620 508,620 508,656 0,656" fill="var(--blue)"/>
    <polygon points="130,600 508,600 508,612 150,612" fill="var(--orange)"/>
    <polygon points="0,560 40,580 40,656 0,656" fill="var(--orange)"/>
  </svg>

  <h2 class="back__title">Our Services</h2>
  <div class="back__lead">
    <em>Family owned and operated, we perform all levels of building and remodeling.</em>
    <p>We offer start-to-finish solutions for every project. We specialize in interior or exterior home renovations, including bathroom and kitchen remodeling, home additions, garages and more!</p>
  </div>

  <svg class="gallery" viewBox="0 0 274 300">
    <rect x="0" y="0" width="274" height="300" fill="var(--blue)"/>
    <g role="img" aria-label="Kitchen with stainless appliances">
      <polygon points="6,16 250,16 6,290" fill="#9a958e"/>
    </g>
    <g role="img" aria-label="Bathroom with tub and vanity">
      <polygon points="268,30 268,286 40,286" fill="#cfcac2"/>
    </g>
    <polygon points="250,16 262,16 18,290 6,290" fill="var(--orange)"/>
    <polygon points="0,0 150,0 140,14 0,14" fill="var(--orange)"/>
    <polygon points="70,286 274,286 274,300 60,300" fill="var(--blue-dark)"/>
  </svg>
  <span class="gallery__label" style="left:236px;top:46px">Bathroom</span>
  <span class="gallery__label" style="left:418px;top:332px">Kitchen</span>

  <p class="back__guarantee">We guarantee high-quality construction for each and every project. Check out samples of our recent work, and you'll agree that we're the best choice for your home renovation project.</p>

  <ul class="services">
    <li><svg width="16" height="16"><use href="#tick"/></svg>NEW CONSTRUCTION</li>
    <li><svg width="16" height="16"><use href="#tick"/></svg>REPAIRS</li>
    <li><svg width="16" height="16"><use href="#tick"/></svg>BARNS</li>
    <li><svg width="16" height="16"><use href="#tick"/></svg>KITCHENS</li>
    <li><svg width="16" height="16"><use href="#tick"/></svg>REMODELS</li>
    <li><svg width="16" height="16"><use href="#tick"/></svg>BATHROOMS</li>
    <li><svg width="16" height="16"><use href="#tick"/></svg>RENOVATIONS</li>
    <li><svg width="16" height="16"><use href="#tick"/></svg>BANK REMODELS</li>
  </ul>

  <div class="back__brand">
    <span class="brand__mark"></span>
    <div class="brand__name">BRIGHTFIELD</div>
    <div class="brand__sub">BUILDERS</div>
  </div>
</section>
</body>
</html>
```